Clarivex glass & hardware manufacturer

Need a SEO friendly, modern & professional looking website. We are selling all kinds of glass & accessories ( Glass/ Mirror/ splash back/ pool fence/ balustrade/ hardware...we are specialised on some special glass, like curve glass,tinted glass thermal & accoustic glass...) It should has simple & crisp feeling like a glass. It must be fully functional with product display and online ordering. Please see attached confirmed logo design(Blue & white). Make sure the theme color match its feel.

Target Market(s)

Architect and designer, Builder, & Developer

Industry/Entity Type

Manufacturer

Coding

Coded - Design and coding required

Font styles to use
Serif
Sans Serif

Colors

Designer to choose colors to be used in the design.

Requirements
Must have
• Glass & hardware theme and our logo
• Here are some competitor's website for reference. (Borrow ideas but not copy : )
• 1.https://www.lumarta.com.au/about
• 2.http://www.pemberdock.com.au/
• 3.http://www.qtv.com.au/
• 4.http://www.hollowmeadfittings.com.au/
Nice to have
• Some transparent or semi transparent effects to make the website like a glass
Should not have
• No limitation for your imagination

```html
<!DOCTYPE html>
<html lang="en">
<head>
<meta charset="utf-8">
<title>Clarivex Glass &amp; Hardware</title>
<link href="https://fonts.googleapis.com/css2?family=Open+Sans:wght@400;600;700&family=Roboto:wght@400;500;700&family=Russo+One&display=swap" rel="stylesheet">
<style>
:root{
  --blue:#1f8fdc;
  --blue-deep:#0b4ea8;
  --blue-dark:#0a3f86;
  --sky:#4aa3e6;
  --ink:#1b1b1b;
  --muted:#777;
  --line:#c9ced3;
  --pale:#eef4f9;
  --white:#fff;
  --star:#f6c21a;
}
*{box-sizing:border-box;margin:0;padding:0}
html,body{width:1200px;height:3035px;overflow:hidden}
body{position:relative;font-family:"Open Sans",Arial,sans-serif;color:var(--ink);background:var(--white)}
.abs{position:absolute}
.section{position:absolute;left:0;width:1200px}

/* hero */
.hero{top:0;height:650px;background:linear-gradient(160deg,#8fc4ea 0%,#3a8fd3 40%,#1b5fae 75%,#0b2f6a 100%)}
.hero-band{left:190px;top:222px;width:820px;height:230px;background:rgba(40,130,220,.55)}
.brand{left:97px;top:50px;display:flex;align-items:center;gap:12px;color:var(--white)}
.brand-mark{width:50px;height:50px;background:var(--white);border-radius:4px}
.brand-name{font-family:"Roboto",sans-serif;font-weight:700;font-size:30px;letter-spacing:1px;line-height:1}
.brand-sub{font-family:"Roboto",sans-serif;font-size:13px;letter-spacing:3px;margin-top:3px}
.nav{left:457px;top:72px;display:flex;gap:0;font-family:"Roboto",sans-serif;font-size:14px;font-weight:500;color:var(--white)}
.nav span{margin-right:44px}
.cart{left:1062px;top:60px;width:40px;height:40px;border:2px solid var(--white);border-radius:50%}
.hero-title{left:0;width:1200px;top:245px;text-align:center;font-family:"Russo One",sans-serif;font-size:46px;color:var(--white);letter-spacing:1px}
.hero-sub{left:0;width:1200px;top:318px;text-align:center;font-size:16px;font-weight:600;color:var(--white)}
.hero-btn{left:504px;top:372px;width:192px;height:50px;border:2px solid var(--white);border-radius:25px;color:var(--white);font-family:"Roboto",sans-serif;font-weight:700;font-size:16px;text-align:center;line-height:46px}
.dots{left:560px;top:550px;display:flex;gap:12px}
.dots i{display:block;width:12px;height:12px;border:2px solid var(--white);border-radius:50%}
.dots i.on{background:var(--white)}
.hero-cut{left:0;top:540px}

/* welcome */
.welcome{top:650px;height:640px;background:linear-gradient(180deg,#f1f6fa,#f7fafc)}
.h2{left:0;width:1200px;text-align:center;font-family:"Roboto",sans-serif;font-weight:700;font-size:42px}
.welcome .h2{top:80px}
.lead{left:210px;width:780px;top:150px;text-align:center;font-size:14px;line-height:28px;color:#555}
.feature{top:250px;width:240px;text-align:center}
.feature-ring{margin:0 auto;width:158px;height:158px;border:2px solid #a9b1b8;border-radius:50%;display:flex;align-items:center;justify-content:center}
.feature h3{margin-top:28px;font-size:21px;font-weight:600;color:#222}
.feature p{margin-top:14px;font-size:14px;line-height:25px;color:var(--muted)}

/* specialized */
.special{top:1290px;height:543px;background:linear-gradient(135deg,#2e7fcb,#4aa6e8 50%,#2b7cc7)}
.special .h2{top:92px;color:var(--white);font-weight:500}
.card{top:177px;width:325px;height:266px}
.card-label{position:absolute;left:0;bottom:28px;width:100%;text-align:center;color:var(--white);font-size:19px;font-weight:700}

/* testimonials */
.tests{top:1833px;height:452px;background:linear-gradient(180deg,#f3f3f3,#e9ecee)}
.tests .h2{top:85px;font-weight:500}
.quote{top:183px;width:320px}
.avatar{position:absolute;left:0;top:0;width:70px;height:70px;border-radius:50%;border:3px solid var(--white);background:#b7a89b}
.qtext{position:absolute;left:90px;top:6px;width:225px;font-size:12px;font-style:italic;line-height:23px;color:#888}
.qtext b{color:var(--blue);font-size:16px;margin-right:6px}
.qname{position:absolute;left:92px;top:0;margin-top:0;font-size:10px;font-weight:700;color:#333}
.qrole{position:absolute;font-size:9px;font-style:italic;color:#333}
.stars{position:absolute;color:var(--star);font-size:20px;letter-spacing:2px}
.arrow-btn{width:34px;height:34px;border:1px solid #aaa;border-radius:50%;top:254px}

/* partners */
.partners{top:2285px;height:163px;background:var(--white);border-top:1px solid #e3e3e3}
.partner{top:37px;width:155px;height:88px;background:var(--white);box-shadow:0 0 6px rgba(0,0,0,.12);display:flex;align-items:center;justify-content:center;gap:8px;font-family:"Roboto",sans-serif;font-weight:700;font-size:20px;color:#222}
.partner i{display:block;width:16px;height:16px;background:#222;border-radius:50%}

/* gallery */
.gallery{top:2448px;height:195px}
.shot{top:0;height:195px;width:230px}
.nudge{top:77px;width:40px;height:42px;background:rgba(60,60,60,.6)}

/* footer */
.footer{top:2643px;height:392px;background:linear-gradient(180deg,#f2f6fa,#e7eef5)}
.foot-brand{left:97px;top:135px;display:flex;align-items:center;gap:12px;color:var(--blue-deep)}
.foot-brand .brand-mark{background:var(--blue)}
.foot-col h4{font-family:"Roboto",sans-serif;font-weight:500;font-size:19px;color:#222}
.links li{list-style:none;font-size:12px;color:#444;line-height:25px}
.foot-text{font-size:12px;color:#444;line-height:22px}
.email{width:255px;border-bottom:1px solid #999;font-size:12px;color:#999;padding:0 0 8px 10px}
.sub-btn{width:106px;height:30px;border-radius:15px;background:var(--blue);color:var(--white);font-size:11px;font-weight:700;text-align:center;line-height:30px}
.contact-row{display:flex;gap:18px;font-size:12px;color:#444;line-height:18px;margin-bottom:18px}
.contact-row svg{flex:none;margin-top:2px}
.rule{left:97px;top:320px;width:1006px;border-top:1px solid #bfc8d2}
.copy{left:97px;top:348px;font-size:12px;color:#444}
.social{top:340px;width:30px;height:30px;border-radius:50%;background:var(--blue-dark)}
</style>
</head>
<body>

<header class="section hero" role="img" aria-label="Upward view of a glass office tower against a blue sky">
  <div class="abs hero-band"></div>
  <div class="abs brand">
    <div class="brand-mark"></div>
    <div><div class="brand-name">CLARIVEX</div><div class="brand-sub">GLASS &amp; HARDWARE</div></div>
  </div>
  <nav class="abs nav"><span>HOME</span><span>ABOUT US</span><span>PRODUCTS</span><span>SERVICES</span><span>BLOG</span><span>CONTACT US</span></nav>
  <div class="abs cart">
    <svg width="36" height="36" viewBox="0 0 36 36"><path d="M11 13h3l2 9h8l2-7H15" fill="none" stroke="#fff" stroke-width="2"/><circle cx="17" cy="25" r="1.5" fill="#fff"/><circle cx="23" cy="25" r="1.5" fill="#fff"/></svg>
  </div>
  <h1 class="abs hero-title">Clarivex glass &amp; hardwares</h1>
  <p class="abs hero-sub">we are specialised on some special glass, like curve glass, tinted glass thermal &amp; acoustic glass</p>
  <div class="abs hero-btn">GET MORE INFO</div>
  <div class="abs dots"><i class="on"></i><i></i><i></i><i></i></div>
  <svg class="abs hero-cut" width="1200" height="110" viewBox="0 0 1200 110">
    <polygon points="0,0 600,95 1200,0 1200,110 0,110" fill="#0b4ea8"/>
    <polygon points="0,14 600,100 1200,14 1200,110 0,110" fill="#f1f6fa"/>
  </svg>
</header>

<section class="section welcome">
  <h2 class="abs h2">Welcome !</h2>
  <p class="abs lead">Nam libero tempore, cum soluta nobis est eligendi optio cumque nihil impedit quo minus id quod maxime placeat facere possimus, omnis voluptas assumenda est, omnis dolor repellend us autem quibusdam et.</p>
  <div class="abs feature" style="left:87px">
    <div class="feature-ring"><svg width="70" height="70" viewBox="0 0 70 70"><rect x="8" y="32" width="12" height="26" rx="2" fill="#1f8fdc"/><path d="M23 34l12-20c4-2 7 1 6 5l-3 9h18c4 0 6 4 4 7l-6 19c-1 3-3 4-6 4H23z" fill="#1f8fdc"/></svg></div>
    <h3>Quality</h3><p>Nam libero tem um soluta no bis est eligendi optio cumque nihil impedit quo minus id</p>
  </div>
  <div class="abs feature" style="left:349px">
    <div class="feature-ring"><svg width="80" height="70" viewBox="0 0 80 70"><path d="M40 66L8 34C-2 22 6 4 22 4c8 0 14 5 18 11C44 9 50 4 58 4c16 0 24 18 14 30z" fill="#1f8fdc"/></svg></div>
    <h3>Wellness</h3><p>Nam libero tem um soluta no bis est eligendi optio cumque nihil impedit quo minus id</p>
  </div>
  <div class="abs feature" style="left:611px">
    <div class="feature-ring"><svg width="50" height="70" viewBox="0 0 50 70"><path d="M25 4C12 4 4 14 4 24c0 9 8 14 10 22h22c2-8 10-13 10-22C46 14 38 4 25 4z" fill="none" stroke="#1f8fdc" stroke-width="4"/><path d="M19 30l6 8 6-8M25 38v8" fill="none" stroke="#1f8fdc" stroke-width="3"/><rect x="15" y="50" width="20" height="5" fill="#1f8fdc"/><rect x="17" y="58" width="16" height="5" fill="#1f8fdc"/></svg></div>
    <h3>Smart Connected</h3><p>Nam libero tem um soluta no bis est eligendi optio cumque nihil impedit quo minus id</p>
  </div>
  <div class="abs feature" style="left:873px">
    <div class="feature-ring"><svg width="76" height="70" viewBox="0 0 76 70"><path d="M30 6h16l8 14 6-3-6 17-17-3 6-3-7-12-8 13-10-6z" fill="#1f8fdc"/><path d="M6 44l8-14 10 6-7 12h15v-7l11 13-11 13v-6H14c-6 0-10-9-8-17z" fill="#1f8fdc"/><path d="M56 32l12 8c4 8-1 19-8 19H50l-1 0 8-14z" fill="#1f8fdc"/></svg></div>
    <h3>Sustainable</h3><p>Nam libero tem um soluta no bis est eligendi optio cumque nihil impedit quo minus id</p>
  </div>
</section>

<section class="section special">
  <h2 class="abs h2">We are specialized in</h2>
  <div class="abs card" style="left:99px;background:linear-gradient(160deg,#9aa9b3,#4a5761 60%,#1d2329)" role="img" aria-label="Curved glass facade seen from below"><span class="card-label">CURVE GLASS</span></div>
  <div class="abs card" style="left:439px;background:linear-gradient(180deg,#cfe2ee,#7fa8c4 55%,#1e2b34)" role="img" aria-label="Tinted glass curtain wall interior"><span class="card-label">TINTED GLASS</span></div>
  <div class="abs card" style="left:778px;background:linear-gradient(180deg,#8fb4cf,#6b6f6a 50%,#2a2f2f)" role="img" aria-label="Apartment building with thermal and acoustic glazing"><span class="card-label">THERMAL &amp; ACOUSTIC GLASS</span></div>
</section>

<section class="section tests">
  <h2 class="abs h2">Client Testimonials</h2>
  <div class="abs arrow-btn" style="left:31px"><svg width="32" height="32"><path d="M18 10l-6 6 6 6" fill="none" stroke="#888" stroke-width="1.5"/></svg></div>
  <div class="abs arrow-btn" style="left:1135px"><svg width="32" height="32"><path d="M14 10l6 6-6 6" fill="none" stroke="#888" stroke-width="1.5"/></svg></div>

  <div class="abs quote" style="left:98px">
    <div class="avatar" role="img" aria-label="Client portrait"></div>
    <p class="qtext"><b>“</b>At vero eos et accusamus et iustodio dignissimos ducimus qui blanditiipraesnt ium voluptatum deleniti atq.</p>
    <div class="qname" style="left:92px;top:0;margin-top:0;position:absolute;top:0"></div>
    <div class="qname" style="top:100px;left:92px">MIRELA FONTANE</div>
    <div class="qrole" style="top:117px;left:92px">Financial Services Professional</div>
    <div class="stars" style="top:145px;left:88px">★★★★☆</div>
  </div>
  <div class="abs quote" style="left:448px">
    <div class="avatar" role="img" aria-label="Client portrait" style="background:#9a9a9a"></div>
    <p class="qtext"><b>“</b>At vero eos et accusamus et iustodio dignissimos ducimus qui blanditiipraesnt ium voluptatum deleniti atq.</p>
    <div class="qname" style="top:100px;left:92px">TEODOR V. HALVARD</div>
    <div class="qrole" style="top:117px;left:92px">Regional Urban Fellow at the Kestwick</div>
    <div class="stars" style="top:145px;left:88px">★★★★★</div>
  </div>
  <div class="abs quote" style="left:793px">
    <div class="avatar" role="img" aria-label="Client portrait" style="background:#c8b9a8"></div>
    <p class="qtext"><b>“</b>At vero eos et accusamus et iustodio dignissimos ducimus qui blanditiipraesnt ium voluptatum deleniti atq.</p>
    <div class="qname" style="top:100px;left:92px">IRIS CALLOWAY</div>
    <div class="qrole" style="top:117px;left:92px">Creative Strategist | Entrepreneur &amp; Upcoming</div>
    <div class="stars" style="top:145px;left:88px">★★★★☆</div>
  </div>
</section>

<section class="section partners">
  <svg class="abs" style="left:68px;top:70px" width="20" height="24"><path d="M13 4l-8 8 8 8" fill="none" stroke="#333" stroke-width="2"/></svg>
  <svg class="abs" style="left:1112px;top:70px" width="20" height="24"><path d="M7 4l8 8-8 8" fill="none" stroke="#333" stroke-width="2"/></svg>
  <div class="abs partner" style="left:115px"><i></i>Kestrel</div>
  <div class="abs partner" style="left:278px">Norvane</div>
  <div class="abs partner" style="left:441px"><i></i>Hearthline</div>
  <div class="abs partner" style="left:604px">Dunmore</div>
  <div class="abs partner" style="left:767px"><i></i>quillwork</div>
  <div class="abs partner" style="left:930px">R.T. Ledger</div>
</section>

<section class="section gallery">
  <div class="abs shot" style="left:0;background:linear-gradient(135deg,#f3d9a0,#7c9fb4 55%,#3e5566)" role="img" aria-label="Glass balustrade at sunset"></div>
  <div class="abs shot" style="left:242px;background:linear-gradient(180deg,#5d95c9,#b9d6ee 60%,#e6eef5)" role="img" aria-label="Glass tower reflecting clouds"></div>
  <div class="abs shot" style="left:484px;background:linear-gradient(180deg,#dfe9ec,#9fb4a3 60%,#5f6f66)" role="img" aria-label="Glass shopfront entrance"></div>
  <div class="abs shot" style="left:726px;background:linear-gradient(135deg,#1f5fa8,#5fa0dd 55%,#cfe3f4)" role="img" aria-label="Glass roof lattice from below"></div>
  <div class="abs shot" style="left:968px;width:232px;background:linear-gradient(135deg,#e8c660,#a9a196 55%,#5e5a55)" role="img" aria-label="Kitchen with yellow glass splashback"></div>
  <div class="abs nudge" style="left:0"><svg width="40" height="42"><path d="M23 14l-7 7 7 7" fill="none" stroke="#fff" stroke-width="2"/></svg></div>
  <div class="abs nudge" style="left:1160px"><svg width="40" height="42"><path d="M17 14l7 7-7 7" fill="none" stroke="#fff" stroke-width="2"/></svg></div>
</section>

<footer class="section footer">
  <div class="abs foot-brand">
    <div class="brand-mark"></div>
    <div><div class="brand-name">CLARIVEX</div><div class="brand-sub">GLASS &amp; HARDWARE</div></div>
  </div>
  <div class="abs foot-col" style="left:425px;top:75px">
    <h4>Quick Links</h4>
    <ul class="links" style="margin-top:16px"><li>Home</li><li>About us</li><li>Products</li><li>Services</li><li>Terms Of Use</li><li>Privacy Statement</li></ul>
  </div>
  <div class="abs foot-col" style="left:607px;top:75px">
    <h4>Newsletter Subscription</h4>
    <p class="foot-text" style="margin-top:20px;width:230px">Register your Email Address to get information about us</p>
    <div class="email" style="margin-top:20px">Email Address</div>
    <div class="sub-btn" style="margin-top:20px">SUBSCRIBE</div>
  </div>
  <div class="abs foot-col" style="left:917px;top:75px">
    <h4>Contact Us</h4>
    <div style="margin-top:24px">
      <div class="contact-row"><svg width="12" height="16"><path d="M6 15C2 9 1 7 1 5a5 5 0 0110 0c0 2-1 4-5 10z" fill="#1f8fdc"/><circle cx="6" cy="5" r="2" fill="#fff"/></svg><span>27, quasi archbeatae vitae<br>dicta sunt explicabo</span></div>
      <div class="contact-row"><svg width="14" height="14"><path d="M3 1l3 3-2 2c1 2 2 3 4 4l2-2 3 3-2 2C6 13 1 8 1 3z" fill="#1f8fdc"/></svg><span>1 800 555 014</span></div>
      <div class="contact-row"><svg width="14" height="14"><rect x="1" y="4" width="12" height="9" fill="#1f8fdc"/><rect x="4" y="1" width="6" height="4" fill="#1f8fdc"/></svg><span>1 800 555 015</span></div>
      <div class="contact-row"><svg width="14" height="12"><rect x="0" y="1" width="14" height="10" fill="#1f8fdc"/><path d="M0 1l7 6 7-6" fill="none" stroke="#fff" stroke-width="1.2"/></svg><span>info@clarivex.com</span></div>
    </div>
  </div>
  <div class="abs rule"></div>
  <p class="abs copy">Copyrights © 2018, Clarivex glass &amp; hardwares. All rights reserved.</p>
  <div class="abs social" style="left:960px"></div>
  <div class="abs social" style="left:996px;background:var(--blue)"></div>
  <div class="abs social" style="left:1032px;background:var(--blue-deep)"></div>
  <div class="abs social" style="left:1068px;background:var(--sky)"></div>
</footer>

</body>
</html>
```